Flooring & Interior Design showroom

Just bought this business- Kestrel Lane Flooring & Interiors. Love our logo (we are on Kestrel Lane )and colors
Forest green, gold and black
Love that the back lists everything we do. We no longer have plenotilex but need to add in LVP/ SPC and need to take out vantor shadehub logo at the bottom and use the quib logo instead (maybe? open to suggestions)

Not in love with our cards- I want a higher end look
I hate the gradient poop color we have now.
Would love if they were all black - maybe or ??
or had a foil or embossing?

```html
<!DOCTYPE html>
<html lang="en">
<head>
<meta charset="utf-8">
<title>Kestrel Lane Flooring &amp; Interiors – Business Card</title>
<link rel="stylesheet" href="https://fonts.googleapis.com/css2?family=Cinzel:wght@600&family=Open+Sans:wght@400;600;700&display=swap">
<style>
  :root {
    --charcoal: #58595b;
    --charcoal-dark: #464749;
    --gold: #d9b873;
    --forest: #2e8b3f;
    --cream: #f3ead2;
    --page: #e9e7e2;
  }
  * { margin: 0; padding: 0; box-sizing: border-box; }
  html, body { width: 1200px; height: 900px; overflow: hidden; }
  body {
    background: var(--page);
    font-family: "Open Sans", Arial, sans-serif;
    position: relative;
  }
  .card {
    position: absolute;
    left: 285px;
    width: 630px;
    height: 360px;
    overflow: hidden;
    box-shadow: 0 6px 18px rgba(0,0,0,0.18);
  }
  .card--front { top: 50px; background: var(--charcoal); }
  .card--back  { top: 480px; background: var(--gold); }

  /* Front */
  .front__band {
    position: absolute; left: 0; right: 0; top: 222px; height: 84px;
    background: var(--gold);
  }
  .front__rule {
    position: absolute; left: 0; right: 0; top: 306px; height: 6px;
    background: var(--charcoal-dark);
  }
  .front__strip {
    position: absolute; left: 0; right: 0; top: 312px; height: 12px;
    background: var(--gold);
  }
  .brand {
    position: absolute;
    display: flex; align-items: center; gap: 10px;
    color: var(--forest);
    font-family: "Cinzel", Georgia, serif;
    font-weight: 600;
    line-height: 1.15;
  }
  .brand__dot {
    width: 14px; height: 14px; border-radius: 50%;
    background: var(--forest); flex: none;
  }
  .brand--front {
    left: 0; right: 0; top: 140px; justify-content: center;
    color: var(--gold); font-size: 22px; text-align: center;
  }
  .brand--front .brand__dot { background: var(--gold); }
  .person {
    position: absolute; left: 0; right: 0; top: 238px;
    text-align: center; color: var(--charcoal-dark);
  }
  .person__name { font-weight: 700; font-size: 20px; }
  .person__title { font-size: 13px; margin-top: 2px; }

  /* Back */
  .signs {
    position: absolute;
    display: flex; flex-direction: column; gap: 3px;
  }
  .signs--right { right: 0; top: 14px; align-items: flex-end; }
  .signs--left  { left: 0; top: 158px; align-items: flex-start; }
  .sign {
    height: 18px; background: var(--forest);
    color: var(--cream); font-size: 11.5px; font-weight: 600;
    display: flex; align-items: center; line-height: 1;
  }
  .signs--right .sign {
    justify-content: flex-end; padding-right: 8px;
    clip-path: polygon(14px 0, 100% 0, 100% 100%, 14px 100%, 0 50%);
  }
  .signs--left .sign {
    padding-left: 8px;
    clip-path: polygon(0 0, calc(100% - 14px) 0, 100% 50%, calc(100% - 14px) 100%, 0 100%);
  }
  .brand--back {
    left: 185px; top: 86px; width: 270px; font-size: 19px;
  }
  .tagline {
    position: absolute; left: 209px; top: 140px;
    color: var(--forest); font-size: 13px; font-weight: 600;
  }
  .contact {
    position: absolute; right: 28px; bottom: 16px;
    color: var(--charcoal-dark); font-size: 12px; line-height: 1.5;
    font-style: normal; text-align: right;
  }
</style>
</head>
<body>

  <section class="card card--front" aria-label="Business card front">
    <div class="front__band"></div>
    <div class="front__rule"></div>
    <div class="front__strip"></div>
    <div class="brand brand--front">
      <span class="brand__dot"></span>
      <span class="brand__name">Kestrel Lane Flooring &amp; Interiors</span>
    </div>
    <div class="person">
      <p class="person__name">Owen Hartley</p>
      <p class="person__title">Salesperson</p>
    </div>
  </section>

  <section class="card card--back" aria-label="Business card back">
    <div class="signs signs--right">
      <span class="sign" style="width:150px">Pleated Shades</span>
      <span class="sign" style="width:120px">Pillows</span>
      <span class="sign" style="width:140px">Bed Spreads</span>
      <span class="sign" style="width:130px">Shutters</span>
      <span class="sign" style="width:110px">Draperies</span>
      <span class="sign" style="width:145px">Upholstery</span>
      <span class="sign" style="width:125px">LVP / SPC</span>
      <span class="sign" style="width:150px">Verticals</span>
      <span class="sign" style="width:105px">Fabric</span>
    </div>

    <div class="brand brand--back">
      <span class="brand__dot"></span>
      <span class="brand__name">Kestrel Lane<br>Flooring &amp; Interiors</span>
    </div>
    <p class="tagline">Home Town Service Since 1979</p>

    <div class="signs signs--left">
      <span class="sign" style="width:140px">Area Rugs</span>
      <span class="sign" style="width:115px">Hardwood</span>
      <span class="sign" style="width:150px">Blinds</span>
      <span class="sign" style="width:125px">Laminate</span>
      <span class="sign" style="width:160px">Carpet</span>
      <span class="sign" style="width:110px">Sheers</span>
      <span class="sign" style="width:145px">Cork</span>
      <span class="sign" style="width:105px">Vinyl</span>
      <span class="sign" style="width:150px">Valances</span>
    </div>

    <address class="contact">
      Store 831.555.0142 Cell 559-555-0178 Fax 831.555.0193<br>
      314 Kestrel Lane, Alder Cove CA 93901<br>
      owen@kestrellaneflooring.com
    </address>
  </section>

</body>
</html>
```